Business Card + Stationery Design for a Craft Beer Bar

Mr. Tovell's is a taproom sport bar that contains in its menu beers from different places around the world. What we offer differently is the experience that you can get inside our location, ambient music with rock from the 80s to 90s, projection with the sports of the moment, board games and private events.

Target Market(s)

Young people, Mid and High Class

Industry/Entity Type

Business

Font styles to use
Serif
Sans Serif

Colors
fee18a

Requirements
Must have
• Name, Title, Contact Details, Website
Nice to have
• Mail Signature
Should not have
• n/a

```html
<!DOCTYPE html>
<html lang="en">
<head>
<meta charset="utf-8">
<title>Mr. Tovell's — Business Card</title>
<link rel="stylesheet" href="https://fonts.googleapis.com/css2?family=Roboto:wght@400;500&display=swap">
<style>
  :root {
    --page: #e9e6e1;
    --card: #1b1b1b;
    --card-edge: #101010;
    --gold: #fee18a;
    --gold-deep: #d9b85a;
    --white: #f4f4f4;
    --muted: #bdbdbd;
  }
  * { box-sizing: border-box; margin: 0; padding: 0; }
  html, body { width: 1200px; height: 1023px; overflow: hidden; }
  body {
    background: var(--page);
    font-family: "Roboto", Arial, sans-serif;
    position: relative;
  }
  .card {
    position: absolute;
    width: 700px;
    height: 400px;
    border-radius: 22px;
    background: linear-gradient(160deg, #242424 0%, var(--card) 55%, var(--card-edge) 100%);
    box-shadow: 0 18px 40px rgba(0,0,0,.28);
    overflow: hidden;
    color: var(--white);
  }
  .card--front { left: 250px; top: 70px; }
  .card--back { left: 250px; top: 553px; }

  .gold-band {
    position: absolute; left: 0; right: 0; bottom: 0; height: 16px;
    background: linear-gradient(90deg, var(--gold-deep), var(--gold));
  }

  .brand {
    position: absolute;
    font-family: "Roboto", Arial, sans-serif;
    font-weight: 500;
    color: var(--white);
    line-height: 1;
    white-space: nowrap;
    display: flex; align-items: center; gap: 14px;
  }
  .brand-dot { width: 14px; height: 14px; border-radius: 50%; background: var(--gold); flex: none; }
  .card--front .brand { right: 56px; top: 78px; font-size: 40px; }
  .card--back .brand { left: 50%; top: 50%; transform: translate(-50%, -50%); font-size: 56px; }
  .card--back .brand-dot { width: 18px; height: 18px; }

  .person { position: absolute; left: 58px; top: 160px; }
  .person-marker {
    position: absolute; left: -58px; top: 4px;
    width: 34px; height: 56px;
  }
  .person-name { font-size: 30px; font-weight: 500; color: var(--gold); line-height: 1.1; }
  .person-title { font-size: 17px; color: var(--muted); margin-top: 8px; }

  .contacts { position: absolute; left: 58px; bottom: 52px; list-style: none; }
  .contacts li { display: flex; align-items: center; gap: 12px; font-size: 19px; margin-top: 8px; white-space: nowrap; }
  .icon { width: 18px; height: 18px; flex: none; }
</style>
</head>
<body>

<article class="card card--front">
  <div class="brand"><span class="brand-dot"></span>Mr. Tovell's</div>

  <div class="person">
    <svg class="person-marker" viewBox="0 0 34 56" aria-hidden="true">
      <polygon points="34,0 34,56 0,56" fill="var(--white)"/>
    </svg>
    <p class="person-name">Your Name</p>
    <p class="person-title">Your Title</p>
  </div>

  <ul class="contacts">
    <li>
      <svg class="icon" viewBox="0 0 20 20" aria-hidden="true"><circle cx="10" cy="10" r="10" fill="var(--gold)"/><path d="M7 5.5c.6 0 1 1.6 1 2 0 .6-.9.9-.6 1.5.5 1 1.4 1.9 2.4 2.4.6.3.9-.6 1.5-.6.4 0 2 .4 2 1 0 1-1 1.8-2 1.7C8.5 13.2 6.3 11 6 8c-.1-1 .5-2.5 1-2.5z" fill="var(--card)"/></svg>
      555-204-7316
    </li>
    <li>
      <svg class="icon" viewBox="0 0 20 20" aria-hidden="true"><rect x="1" y="4" width="18" height="12" fill="var(--gold)"/><path d="M1 4l9 7 9-7" fill="none" stroke="var(--card)" stroke-width="1.5"/></svg>
      jmarlow@mrtovells.com
    </li>
    <li>
      <svg class="icon" viewBox="0 0 20 20" aria-hidden="true"><circle cx="10" cy="10" r="10" fill="var(--gold)"/><path d="M2 10h16M10 1c-4 4-4 14 0 18M10 1c4 4 4 14 0 18" fill="none" stroke="var(--card)" stroke-width="1.3"/></svg>
      www.mrtovells.com
    </li>
  </ul>

  <div class="gold-band"></div>
</article>

<article class="card card--back">
  <div class="brand"><span class="brand-dot"></span>Mr. Tovell's</div>
</article>

</body>
</html>
```